Dr. Lumora needs a design for its website!

*Only need the design, coding is not required.
*Need desktop version ($500) and mobile/tablet version ($200)
*The attached files are not the exact layout we want, they are just for you to know what information should be included in those pages.
*The function of our website is like www.qtv-medlist.example
*For the background picture, prefer a lively picture and chinese people in it, NOT necessarily need a doctor or sick person in the picture

***Don't just copy the layout from the attachments or from the reference website, we are looking for creative ideas, non-ordinary designs!!!****

We are developing a website for the public to search a doctor by different criteria. At the initial stage, we need 4 pages to start with and other pages at later stage. I have attached the general idea of these pages but not necessarily to be exactly the same, I am looking for some new ideas.

This website needs a professional, modern, simple and user friendly design. The main color to be used in the website will be same as the color (R:0 G:139 B:205) used in our logo (see attached). We don't have any particular thoughts for the other color and the font to be used in the website. Can try to use circle outline for the icon in the navigation bar.

1. Home: will include 4 sections (see attached)

2. Doctor's details (see attached)

3. Health information: will include a short descriptions of this Health Info page and 5 sections (see attached)

4. News (see attached)

Reason: Not too many suitable designs to choose from and need more time to go through the designs

Target Market(s)

All

Industry/Entity Type

Medical

Number of Pages Required

4 page

Requirements
Should not have
• must not be same as or looks too much like www.qtv-medlist.example
• prefer not to use black and red color

```html
<!DOCTYPE html>
<html lang="en">
<head>
<meta charset="utf-8">
<title>Dr. Lumora – Doctors recently updated</title>
<link href="https://fonts.googleapis.com/css2?family=Open+Sans:wght@400;600&display=swap" rel="stylesheet">
<style>
:root{
  --brand:#4a8ac9;
  --brand-text:#3a86c8;
  --ink:#444;
  --muted:#6a6a6a;
  --table-head:#7c7c7c;
  --row-alt:#f7f7f7;
  --search-btn:#0d2f3f;
  --white:#fff;
}
*{box-sizing:border-box;margin:0;padding:0}
html,body{width:1042px;height:1200px;overflow:hidden}
body{font-family:"Open Sans",Arial,sans-serif;color:var(--ink);background:var(--white);position:relative}
.site-header{height:92px;position:relative}
.brand{position:absolute;left:64px;top:26px;display:flex;align-items:center;gap:8px}
.brand-dot{width:34px;height:34px;border-radius:50%;background:var(--brand)}
.brand-name{font-size:27px;font-weight:600;color:var(--brand)}
.social{position:absolute;left:752px;top:42px;display:flex;gap:18px}
.social span{width:16px;height:16px;border-radius:50%;background:#8a8a8a}
.lang{position:absolute;left:917px;top:45px;display:flex;align-items:center;gap:6px;font-size:10px;color:#555}
.flag{width:20px;height:12px;background:#3b4a8c;border:1px solid #ccc}
.nav{height:50px;background:var(--brand);position:relative}
.nav ul{list-style:none}
.nav li{position:absolute;top:16px;color:var(--white);font-size:13.5px;font-weight:600;line-height:18px}
.search{position:absolute;left:768px;top:11px;width:210px;height:28px;display:flex}
.search input{flex:1;border:0;padding:0 8px;font:12px "Open Sans",sans-serif;color:#999}
.search button{width:31px;border:0;background:var(--search-btn);display:flex;align-items:center;justify-content:center}
.page-title{position:absolute;left:64px;top:180px;font-size:21px;font-weight:400;color:var(--brand-text)}
.doctors{position:absolute;left:65px;top:228px;width:913px;border-collapse:collapse;border:1px solid #e2e2e2;font-size:12.5px}
.doctors th{background:var(--table-head);color:var(--white);font-weight:600;font-size:13px;text-align:left;height:46px;padding-left:5px}
.doctors th:first-child,.doctors td:first-child{padding-left:15px}
.doctors td{height:75px;padding-left:4px;vertical-align:middle;color:var(--ink);line-height:18px}
.doctors td.doctor-name{color:var(--brand-text)}
.doctors tr:nth-child(even) td{background:var(--row-alt)}
.gender{display:flex;align-items:center;gap:12px}
.avatar{width:28px;height:28px;border-radius:50%;background:#d9d9d9;border:1px solid #ddd;flex:none}
.site-footer{position:absolute;left:0;top:837px;width:1042px;height:318px;background:linear-gradient(#f0f0f0,#fafafa);border-top:1px solid #ddd}
.footer-col{position:absolute;top:32px}
.footer-col h3{font-size:15px;font-weight:600;color:var(--brand-text);margin-bottom:4px}
.footer-col li{list-style:none;font-size:11.5px;color:var(--muted);line-height:18px;margin-top:7px}
.apps{position:absolute;left:768px;top:251px;display:flex;gap:12px}
.app-badge{height:32px;border-radius:4px;background:#111}
.copyright{position:absolute;left:0;top:1155px;width:1042px;height:45px;background:var(--brand);color:var(--white);font-size:10.5px;text-align:center;line-height:45px}
</style>
</head>
<body>
<header class="site-header">
  <div class="brand"><span class="brand-dot"></span><span class="brand-name">Dr. Lumora</span></div>
  <div class="social"><span></span><span></span><span></span><span></span></div>
  <div class="lang"><span class="flag"></span>EN
    <svg width="8" height="6" viewBox="0 0 8 6"><path d="M1 1l3 3 3-3" stroke="#666" fill="none"/></svg></div>
</header>
<nav class="nav">
  <ul><li style="left:66px">Home</li><li style="left:155px">TBC</li><li style="left:231px">Health Info</li><li style="left:355px">News</li><li style="left:441px">About Us</li><li style="left:552px">Contact Us</li></ul>
  <form class="search"><input value="Search..." readonly><button type="button" aria-label="Search">
    <svg width="13" height="13" viewBox="0 0 13 13"><circle cx="5.5" cy="5.5" r="4" stroke="#fff" stroke-width="2" fill="none"/><path d="M8.5 8.5l3.5 3.5" stroke="#fff" stroke-width="2"/></svg></button></form>
</nav>

<h1 class="page-title">Doctors recently updated information page</h1>

<table class="doctors">
  <colgroup><col style="width:152px"><col style="width:96px"><col style="width:93px"><col style="width:115px"><col style="width:95px"><col style="width:170px"><col style="width:96px"><col style="width:96px"></colgroup>
  <thead><tr><th>Doctor’s Name</th><th>Gender</th><th>Specialism</th><th>Practice Type</th><th>Experience</th><th>Address</th><th>District</th><th>Phone No.</th></tr></thead>
  <tbody>
    <tr><td class="doctor-name">Meilin Ho Ka<br>Yan Lau</td><td><div class="gender"><span class="avatar" role="img" aria-label="Male doctor icon"></span>Male</div></td><td>Dental</td><td>Private Practice</td><td>3yrs Exp</td><td>1420 Larkfield<br>Lane,Glasgow, G12 7QX</td><td>Glasgow</td><td>555-014-2290</td></tr>
    <tr><td class="doctor-name">Meilin Ho Ka<br>Yan Lau</td><td><div class="gender"><span class="avatar" role="img" aria-label="Female doctor icon"></span>Female</div></td><td>Dental</td><td>Private Practice</td><td>3yrs Exp</td><td>1420 Larkfield<br>Lane,Glasgow, G12 7QX</td><td>Glasgow</td><td>555-014-2290</td></tr>
    <tr><td class="doctor-name">Meilin Ho Ka<br>Yan Lau</td><td><div class="gender"><span class="avatar" role="img" aria-label="Male doctor icon"></span>Male</div></td><td>Dental</td><td>Private Practice</td><td>3yrs Exp</td><td>1420 Larkfield<br>Lane,Glasgow, G12 7QX</td><td>Glasgow</td><td>555-014-2290</td></tr>
    <tr><td class="doctor-name">Meilin Ho Ka<br>Yan Lau</td><td><div class="gender"><span class="avatar" role="img" aria-label="Female doctor icon"></span>Female</div></td><td>Dental</td><td>Private Practice</td><td>3yrs Exp</td><td>1420 Larkfield<br>Lane,Glasgow, G12 7QX</td><td>Glasgow</td><td>555-014-2290</td></tr>
    <tr><td class="doctor-name">Meilin Ho Ka<br>Yan Lau</td><td><div class="gender"><span class="avatar" role="img" aria-label="Male doctor icon"></span>Male</div></td><td>Dental</td><td>Private Practice</td><td>3yrs Exp</td><td>1420 Larkfield<br>Lane,Glasgow, G12 7QX</td><td>Glasgow</td><td>555-014-2290</td></tr>
    <tr><td class="doctor-name">Meilin Ho Ka<br>Yan Lau</td><td><div class="gender"><span class="avatar" role="img" aria-label="Female doctor icon"></span>Female</div></td><td>Dental</td><td>Private Practice</td><td>3yrs Exp</td><td>1420 Larkfield<br>Lane,Glasgow, G12 7QX</td><td>Glasgow</td><td>555-014-2290</td></tr>
    <tr><td class="doctor-name">Meilin Ho Ka<br>Yan Lau</td><td><div class="gender"><span class="avatar" role="img" aria-label="Female doctor icon"></span>Female</div></td><td>Dental</td><td>Private Practice</td><td>3yrs Exp</td><td>1420 Larkfield<br>Lane,Glasgow, G12 7QX</td><td>Glasgow</td><td>555-014-2290</td></tr>
  </tbody>
</table>

<footer class="site-footer">
  <div class="footer-col" style="left:66px;width:220px"><h3>Popular search</h3><ul>
    <li>General</li><li>Obstetrics and gynecology specialist</li><li>Skin and sexually transmitted diseases specialist</li><li>ENT specialist</li><li>Orthopedic specialist</li><li>Eye specialist</li><li>Paediatrics</li><li>dentist</li><li>List of registered chiropractor</li></ul></div>
  <div class="footer-col" style="left:306px"><h3>Specialist</h3><ul>
    <li>Psychiatric Specialist</li><li>Gastrointestinal specialist Hepatology</li><li>Urology Specialist</li><li>Surgical specialties</li><li>Plastic Surgery Specialist</li><li>Practicing physical therapist</li><li>Cardiology specialist</li><li>Neurology specialist</li></ul></div>
  <div class="footer-col" style="left:568px"><h3>Doctor search</h3><ul>
    <li>Search by region</li><li>Search by specialist</li><li>Comprehensive search</li><li>Doctors concentration</li><li>List of doctors</li><li>Medical card plan</li></ul></div>
  <div class="footer-col" style="left:766px"><h3>Health Information</h3><ul>
    <li>Health magazine</li><li>Community News</li><li>Medical center</li><li>Medical organizations</li><li>Patient groups</li><li>Emergency Services</li></ul></div>
  <div class="apps"><span class="app-badge" style="width:90px"></span><span class="app-badge" style="width:107px"></span></div>
</footer>
<div class="copyright">Copyright &nbsp;© 2016. Company Name. All Right Reserved</div>
</body>
</html>
```